Calm Harbor website development

Need a website designed for a coaching business. Very high-end, luxury, professionalism, in the area of STRESS, see brief attached. I have a logo already
Updates

Slow in providing feedback

Target Market(s)

CEOs very successful men and wealthy females, high end luxury market

Industry/Entity Type

coaching

Number of Pages Required

1 page

Requirements
Must have
• Luxury look, professional, serious but warm, appealing to both sexes

```html
<!DOCTYPE html>
<html lang="en">
<head>
<meta charset="utf-8">
<title>Calm Harbor – Lifestyle Coaching</title>
<link rel="stylesheet" href="https://fonts.googleapis.com/css2?family=Poppins:wght@400;500;600;700&family=Lato:wght@400;700&display=swap">
<style>
:root{
  --yellow:#fcc511;
  --blue:#1a82f0;
  --nav-blue:#1e88e5;
  --ink:#1b1b1b;
  --text:#333;
  --bar:#4a4a4a;
  --black:#000;
  --white:#fff;
}
*{margin:0;padding:0;box-sizing:border-box}
html,body{width:1200px;height:2778px;overflow:hidden;background:var(--white)}
body{position:relative;font-family:'Lato',sans-serif;color:var(--text)}
.abs{position:absolute}
.brand{font-family:'Poppins',sans-serif;font-weight:600;letter-spacing:3px;color:var(--ink);white-space:nowrap}
/* top bar */
.topbar{left:0;top:0;width:1200px;height:43px}
.topbar-text{top:12px;font-family:'Lato',sans-serif;font-size:14px;color:var(--white)}
.social-dot{width:14px;height:14px;border-radius:50%;background:var(--white)}
.icon-badge{width:32px;height:32px;border-radius:50%;background:var(--nav-blue)}
/* header */
.logo-mark{left:186px;top:8px;width:40px;height:40px;background:var(--ink)}
.logo-name{left:126px;top:74px;width:162px;text-align:center;font-size:17px}
.nav a{position:absolute;top:76px;font-family:'Poppins',sans-serif;font-size:14px;color:var(--ink);text-decoration:none}
.nav a.active{color:var(--nav-blue)}
.pill{display:flex;align-items:center;border-radius:22px;font-family:'Poppins',sans-serif;font-weight:600;font-size:15px}
.pill .dot{width:34px;height:34px;border-radius:50%;background:#333;margin:0 10px 0 4px;flex:none}
.pill-yellow{background:var(--yellow);color:var(--ink)}
/* hero */
.hero{left:0;top:124px;width:1200px;height:630px;overflow:hidden}
.hero-bg{position:absolute;inset:0;background:linear-gradient(100deg,#1d1d1d 0%,#3a3530 45%,#2a2622 100%)}
.hero-kicker{left:111px;top:298px;font-family:'Poppins',sans-serif;font-size:35px;color:var(--white);font-weight:500}
.hero-title{left:109px;top:345px;font-family:'Poppins',sans-serif;font-size:70px;font-weight:700;color:var(--white);line-height:1.1}
.hero-copy{left:111px;top:433px;font-size:16px;line-height:26px;color:var(--white)}
.btn-start{left:120px;top:507px;width:161px;height:41px;background:var(--white);color:var(--nav-blue);font-size:15px}
.hero-photo{left:718px;top:218px;width:500px;height:496px;border-radius:50%;background:radial-gradient(circle at 40% 45%,#d9c8b2 0%,#b59c82 45%,#8d7a68 100%)}
/* welcome */
.welcome-ring{left:171px;top:842px;width:320px;height:320px;border-radius:50%;background:var(--yellow)}
.welcome-photo{left:163px;top:836px;width:318px;height:318px;border-radius:50%;background:linear-gradient(180deg,#6a6f8f 0%,#b07a86 45%,#e37e57 65%,#5a2d2d 100%)}
.section-title{font-family:'Poppins',sans-serif;font-size:31px;color:var(--ink);font-weight:400}
.section-title b{font-weight:700}
.welcome-text{left:560px;top:898px;width:529px;font-size:16.5px;line-height:25.7px;text-align:justify;color:var(--text)}
/* panels */
.panel{top:1264px;height:471px;text-align:center}
.panel-yellow{left:0;width:598px;background:linear-gradient(180deg,#f8c313 0%,#f2bb10 70%,#e8b414 100%)}
.panel-blue{left:598px;width:602px;background:linear-gradient(180deg,#1f86f2 0%,#1a7fee 100%)}
.panel h2{font-family:'Poppins',sans-serif;font-weight:600;font-size:25px}
.panel p{font-size:16.5px;line-height:26px}
/* benefits */
.benefits-title{left:108px;top:1868px;font-family:'Poppins',sans-serif;font-weight:600;font-size:30px;color:var(--ink)}
.benefits-list{left:108px;top:1918px;width:520px;list-style:none}
.benefits-list li{position:relative;padding-left:27px;font-size:16.3px;line-height:25.7px;color:var(--text);margin-bottom:13px;white-space:nowrap}
.benefits-list li::before{content:"";position:absolute;left:4px;top:10px;width:8px;height:8px;border-radius:50%;background:#1455c0}
.chat{left:1152px;top:2376px;width:50px;height:44px;border-radius:50%;background:var(--nav-blue)}
/* footer */
.footer{left:0;top:2399px;width:1200px;height:379px;background:var(--black);color:var(--white)}
.footer h3{position:absolute;top:86px;font-family:'Poppins',sans-serif;font-weight:500;font-size:18px;letter-spacing:.3px}
.footer .link{position:absolute;font-family:'Poppins',sans-serif;font-size:14.5px}
.footer .brand{color:var(--white)}
.newsletter-input{left:854px;top:135px;width:234px;height:47px;background:var(--white);color:#777;font-size:15px;padding:14px 16px}
.newsletter-btn{left:854px;top:189px;width:123px;height:47px;background:var(--yellow);color:var(--ink);font-family:'Poppins',sans-serif;font-weight:600;font-size:15px;text-align:center;line-height:47px}
.copyright{left:0;top:313px;width:1200px;text-align:center;font-family:'Poppins',sans-serif;font-size:15px}
</style>
</head>
<body>

<!-- top contact bar -->
<svg class="abs topbar" width="1200" height="43" viewBox="0 0 1200 43">
  <polygon points="305,0 1200,0 1200,43 326,43" fill="#4a4a4a"/>
  <line x1="857" y1="8" x2="857" y2="35" stroke="#777"/>
</svg>
<div class="abs social-dot" style="left:345px;top:15px"></div>
<div class="abs social-dot" style="left:387px;top:15px"></div>
<div class="abs social-dot" style="left:432px;top:15px"></div>
<div class="abs social-dot" style="left:478px;top:15px"></div>
<div class="abs social-dot" style="left:524px;top:15px"></div>
<div class="abs icon-badge" style="left:607px;top:5px">
  <svg width="32" height="32" viewBox="0 0 32 32"><rect x="9" y="11" width="14" height="10" fill="#fff"/><polyline points="9,11 16,17 23,11" fill="none" stroke="#1e88e5" stroke-width="1.5"/></svg>
</div>
<div class="abs topbar-text" style="left:652px"><b>Email :</b> info@calmharbor.com</div>
<div class="abs icon-badge" style="left:881px;top:5px">
  <svg width="32" height="32" viewBox="0 0 32 32"><path d="M11 9c1 0 2 2 2.5 3.5.3 1-1 1.5-.8 2.3.6 1.8 2 3.3 3.8 4 .8.2 1.3-1 2.3-.7 1.5.5 3.4 1.5 3.3 2.5-.2 1.6-2 2.5-3.5 2.3C13 22.2 9.6 18.5 9 13.4 8.8 11.8 9.6 9 11 9z" fill="#fff"/></svg>
</div>
<div class="abs topbar-text" style="left:925px"><b>Phone :</b> +1 (555) 014 2290</div>

<!-- header -->
<div class="abs logo-mark"></div>
<div class="abs brand logo-name">CALM HARBOR</div>
<nav class="nav">
  <a class="active" href="#" style="left:476px">HOME</a>
  <a href="#" style="left:573px">ABOUT US</a>
  <a href="#" style="left:697px">WHY ME?</a>
  <a href="#" style="left:813px">BENEFITS</a>
</nav>
<svg class="abs" style="left:919px;top:77px" width="20" height="20" viewBox="0 0 20 20"><circle cx="8" cy="8" r="6" fill="none" stroke="#1e88e5" stroke-width="2.5"/><line x1="12.5" y1="12.5" x2="18" y2="18" stroke="#1e88e5" stroke-width="3"/></svg>
<div class="abs pill pill-yellow" style="left:972px;top:66px;width:115px;height:41px"><span class="dot"></span>LOG IN</div>

<!-- hero -->
<section class="abs hero">
  <div class="hero-bg" role="img" aria-label="Dim photo of a person meditating cross-legged"></div>
  <svg class="abs" style="left:0;top:0" width="1200" height="630" viewBox="0 0 1200 630">
    <path d="M0 560 C300 640 700 630 1200 560 L1200 630 L0 630 Z" fill="#fff"/>
    <path d="M0 560 C300 640 700 625 1200 560 L1200 572 C700 628 300 648 0 580 Z" fill="#fcc511"/>
  </svg>
</section>
<div class="abs hero-photo" role="img" aria-label="Photo of a relaxed woman holding a mug of coffee"></div>
<div class="abs hero-kicker">WELCOME TO</div>
<div class="abs hero-title">HEAD COACH</div>
<p class="abs hero-copy">Lorem ipsum dolor sit amet, consectetur adipiscing elit,<br>sed do eiusmod tempor incididunt ut labore et dolore magna aliqua.</p>
<div class="abs pill btn-start"><span class="dot"></span>GET STARTED</div>
<svg class="abs" style="left:576px;top:692px" width="48" height="14" viewBox="0 0 48 14">
  <circle cx="7" cy="7" r="4.5" fill="#fff"/><circle cx="24" cy="7" r="6" fill="#1e88e5" stroke="#fff" stroke-width="2"/><circle cx="41" cy="7" r="4.5" fill="#fff"/>
</svg>

<!-- welcome -->
<div class="abs welcome-ring"></div>
<div class="abs welcome-photo" role="img" aria-label="Photo of a person meditating on a cliff at sunset"></div>
<h2 class="abs section-title" style="left:560px;top:838px">WELCOME TO <b>CALM HARBOR</b></h2>
<p class="abs welcome-text">Calm Harbor came about due to my desire to help people lead a better and healthier life. Initially, I was involved in the fitness/body side of health. As years passed and my experience grew, I realized how important the mind was in total wellness, and that the mind is all powerful and controlling. Control the mind, control the body and achieve success. Stress can be the most debilating factor in our lives, it is the root cause of so many diseases and costs the US workplace an estimated 300 billion dollars due to loss of productivity.</p>
<div class="abs pill pill-yellow" style="left:560px;top:1133px;width:164px;height:41px"><span class="dot"></span>LEARN MORE</div>

<!-- why me / our client -->
<section class="abs panel panel-yellow" role="img" aria-label="Faded photo of two people running through a golden field">
  <h2 class="abs" style="left:0;top:148px;width:598px;color:var(--ink)">WHY ME</h2>
  <p class="abs" style="left:80px;top:204px;width:438px;color:#3a2c00">Been there done that! Have been through a lot, started businesses, selling a business, law suits, marriage, divorce, second marriage, kids, school, sports, fights, robbed, gun in face, traveled the world, successful, two great kids</p>
</section>
<section class="abs panel panel-blue" role="img" aria-label="Faded photo of a smiling woman walking outdoors">
  <h2 class="abs" style="left:0;top:158px;width:602px;color:var(--white)">OUR CLIENT</h2>
  <p class="abs" style="left:90px;top:210px;width:420px;color:var(--white)">Limited number of clients...different stage of life, empty nester, have a full career...won't be a number</p>
</section>

<!-- benefits -->
<h2 class="abs benefits-title">BENEFITS</h2>
<ul class="abs benefits-list">
  <li>Experience</li>
  <li>Sector expert Health/Wellness. Presented at numerous<br>industry shows and quoted in nationalpublications</li>
  <li>Excellent listener...being in sales for many years, the secret<br>is to really listen...and get to the endgame, and make it feel as<br>if it was their decision. Not sure how to word this as a benefit.</li>
  <li>Access/resources industry professionals, sport psychologist...<br>just spent a few hours with the Mind performance coach for the<br>Harbor City Comets baseball team...I can get the best advice</li>
</ul>
<div class="abs pill pill-yellow" style="left:108px;top:2220px;width:164px;height:41px"><span class="dot"></span>LEARN MORE</div>
<svg class="abs" style="left:680px;top:1820px" width="420" height="496" viewBox="0 0 420 496">
  <polygon points="206,3 414,125 414,375 210,493 3,375 3,125" fill="none" stroke="#1e88e5" stroke-width="2.5"/>
  <polygon points="208,20 404,134 404,366 210,478 13,366 13,134" fill="#c9a46a" role="img" aria-label="Photo of a smiling woman with curly hair in a green sweater"/>
</svg>
<div class="abs chat">
  <svg width="50" height="44" viewBox="0 0 50 44"><circle cx="15" cy="22" r="4" fill="#fff"/><circle cx="25" cy="22" r="4" fill="#fff"/><circle cx="35" cy="22" r="4" fill="#fff"/></svg>
</div>

<!-- footer -->
<footer class="abs footer">
  <div class="abs" style="left:176px;top:74px;width:44px;height:44px;background:#fff"></div>
  <div class="abs brand" style="left:92px;top:174px;width:212px;text-align:center;font-size:20px">CALM HARBOR</div>
  <div class="abs social-dot" style="left:111px;top:231px;width:16px;height:16px"></div>
  <div class="abs social-dot" style="left:149px;top:231px;width:16px;height:16px"></div>
  <div class="abs social-dot" style="left:188px;top:231px;width:16px;height:16px"></div>
  <div class="abs social-dot" style="left:227px;top:231px;width:16px;height:16px"></div>

  <h3 style="left:377px">QUICK LIKS</h3>
  <span class="link" style="left:378px;top:128px">Home</span>
  <span class="link" style="left:378px;top:154px">About us</span>
  <span class="link" style="left:378px;top:180px">Why me?</span>
  <span class="link" style="left:378px;top:206px">Benefits</span>

  <h3 style="left:565px">CONTACT US</h3>
  <svg class="abs" style="left:567px;top:133px" width="16" height="20" viewBox="0 0 16 20"><path d="M8 0a7 7 0 0 1 7 7c0 5-7 13-7 13S1 12 1 7a7 7 0 0 1 7-7z" fill="#fff"/><circle cx="8" cy="7" r="2.5" fill="#000"/></svg>
  <span class="link" style="left:597px;top:130px;line-height:26px">Lorem ipsum dolor sit amet,<br>consectetur</span>
  <svg class="abs" style="left:566px;top:200px" width="20" height="20" viewBox="0 0 20 20"><path d="M4 1c1.5 0 3 3 3.5 4.5.3 1.2-1.3 1.8-1 2.8.8 2.2 2.5 4 4.6 4.8 1 .3 1.6-1.2 2.8-.9 1.7.6 4.3 2 4.1 3.2-.3 2-2.5 3.2-4.4 2.9C7 17.1 2.5 12.6 1.5 6.2 1.2 4 2.3 1 4 1z" fill="#fff"/></svg>
  <span class="link" style="left:597px;top:199px">+1 (555) 014 2290</span>
  <svg class="abs" style="left:567px;top:245px" width="18" height="14" viewBox="0 0 18 14"><rect width="18" height="14" fill="#fff"/><polyline points="0,0 9,7 18,0" fill="none" stroke="#000" stroke-width="1.5"/></svg>
  <span class="link" style="left:597px;top:240px">info@calmharbor.com</span>

  <h3 style="left:853px">SING UP FOR NEWSLETTER</h3>
  <div class="abs newsletter-input">Email Address</div>
  <div class="abs newsletter-btn">SUBMIT</div>

  <div class="abs copyright">©Copyrights 2022 Calm Harbor &nbsp;| &nbsp;&nbsp;All Rights Reserved</div>
</footer>

</body>
</html>
```